Company Website

We require an online clothing store website for construction workwear.
It needs to be easy to read, user friendly, easy to navigate purchasing.
We are after designs incorporating our recently design logo, and colour combinations black white and orange (same as the company logo). Needs to highlight quality, safety and products. Any ideas around highlighting branding are welcome.

Target Market(s)

Construction workers and businesses.

Industry/Entity Type

Construction

Coding

Coded - Design and coding required

Number of Pages Required

5+ page

Colors
EE7325
F08F49
F5BC92
FAE3D3
FDF4ED

Requirements
Must have
• Include all pictures, prices and details of the products we sell. See PDF uploaded to brief.
Nice to have
• Simple access to purchase items. Easy to navigate website layout.

```html
<!DOCTYPE html>
<html lang="en">
<head>
<meta charset="utf-8">
<title>Ironline Workwear</title>
<link href="https://fonts.googleapis.com/css2?family=Roboto:wght@400;500;700&family=Rubik:wght@900&family=Kaushan+Script&display=swap" rel="stylesheet">
<style>
:root{
  --orange:#f25c05;
  --orange-soft:#f08f49;
  --peach:#f5bc92;
  --cream:#f8ece6;
  --dark:#2b2b2b;
  --nav:#262626;
  --text:#333;
  --muted:#666;
  --line:#d9d9d9;
  --white:#fff;
}
*{box-sizing:border-box;margin:0;padding:0}
html,body{width:1200px;height:3477px;overflow:hidden}
body{font-family:'Roboto',sans-serif;color:var(--text);background:var(--white);position:relative}
.wrap{position:absolute;left:111px;width:977px}
.script{font-family:'Kaushan Script',cursive}
.ph{display:block}

/* header */
.header{position:absolute;top:0;left:0;width:1200px;height:74px}
.brand{position:absolute;left:116px;top:18px;font-weight:700;font-size:30px;color:var(--orange);letter-spacing:4px;line-height:1}
.brand small{display:block;font-size:10px;letter-spacing:6px;color:var(--dark);text-align:right;margin-top:2px}
.account{position:absolute;left:690px;top:25px;font-size:15px;display:flex;align-items:center;gap:8px}
.account a{color:var(--orange)}
.cart{position:absolute;left:873px;top:24px}
.search{position:absolute;left:923px;top:22px;width:165px;height:30px;border-radius:15px;background:#d6d6d6;font-size:13px;color:#777;padding:7px 15px}
.search .dot{position:absolute;right:12px;top:7px;width:16px;height:16px;border-radius:50%;background:var(--orange)}
.nav{position:absolute;top:74px;left:0;width:1200px;height:51px;background:var(--nav);display:flex;justify-content:space-between;padding:0 111px;align-items:center;color:#fff;font-size:14px}
.nav span::after{content:"";display:inline-block;margin-left:4px;border:4px solid transparent;border-top-color:#fff;border-bottom:0;vertical-align:2px}

/* hero */
.hero{position:absolute;top:125px;left:0;width:1200px;height:544px}
.hero-copy{position:absolute;left:0;top:0;width:446px;height:544px;background:var(--orange);color:#fff;padding:110px 0 0 110px}
.hero-copy .script{font-size:28px}
.hero-copy h1{font-family:'Rubik',sans-serif;font-weight:900;font-size:56px;line-height:66px;margin-top:14px}
.btn-outline{display:inline-flex;gap:22px;align-items:center;background:#fff;color:var(--muted);font-size:17px;padding:11px 22px;margin-top:18px}
.hero-img{position:absolute;left:446px;top:0;width:754px;height:544px;background:linear-gradient(135deg,#4a4a4e,#2b2b30 55%,#5b3a24)}

/* promos */
.promos{position:absolute;top:673px;left:4px;width:1192px;height:377px;display:flex;gap:5px}
.promo{flex:1;position:relative;color:#fff;overflow:hidden}
.promo.g{background:linear-gradient(160deg,#5b4a38,#c49a3a 55%,#3b2f25)}
.promo.j{background:linear-gradient(120deg,#c94a06,#f07a1a 60%,#a63a06)}
.promo.w{background:linear-gradient(150deg,#263a4f,#b4551a 60%,#1f2c3a)}
.promo .s1{position:absolute;left:32px;top:152px;font-size:22px}
.promo .s2{position:absolute;left:30px;top:180px;font-size:86px;line-height:1}
.promo .btn{position:absolute;left:32px;top:310px;width:170px;height:44px;background:var(--orange);font-size:15px;display:flex;align-items:center;justify-content:center}
.jacket-box{position:absolute;left:220px;top:48px;width:145px;height:300px;border:3px solid #fff;display:flex;flex-direction:column;align-items:center;justify-content:flex-end;padding-bottom:8px}
.jacket-box .v{writing-mode:vertical-rl;transform:rotate(180deg);font-family:'Rubik',sans-serif;font-weight:900;font-size:42px;line-height:44px;position:absolute;top:18px}
.jacket-box .pct{font-family:'Rubik',sans-serif;font-weight:900;font-size:48px;color:#111;line-height:1}
.jacket-box .off{font-weight:700;color:#111;font-size:18px}
.w50{position:absolute;right:40px;top:70px;text-align:right;font-size:84px;line-height:1}
.wcon{position:absolute;right:14px;top:160px;font-size:50px}
.wtag{position:absolute;right:0;top:240px;background:var(--orange);padding:2px 16px;font-size:50px}

/* section titles */
.sec-title{height:52px;border-bottom:1px solid var(--line);position:relative}
.sec-title h2{font-family:'Kaushan Script',cursive;font-weight:400;font-size:30px;color:var(--dark)}
.sec-title h2 em{font-style:normal;color:var(--orange)}
.arrows{position:absolute;right:0;top:28px;display:flex;gap:8px;align-items:center}
.arrows i{display:block;border-radius:50%}
.arrows .a1{width:25px;height:25px;background:var(--orange)}
.arrows .a2{width:19px;height:19px;background:#bbb}

/* featured */
.featured{top:1125px}
.cards{display:flex;gap:10px;margin-top:10px}
.card{width:188px;height:400px;border:1px solid var(--line);text-align:center;padding-top:20px}
.card .img{width:160px;height:170px;margin:0 auto 28px;border-radius:8px}
.card .n{font-size:17px;line-height:25px;color:#555}
.card s{display:block;margin-top:10px;font-size:16px;color:#666}
.card .p{color:var(--orange);font-size:17px;margin-top:6px}
.card .b{margin:14px auto 0;width:172px;height:44px;background:var(--dark);color:#fff;display:flex;align-items:center;justify-content:center;font-size:16px}

/* reviews */
.reviews{top:1638px;height:264px;border:1px solid var(--line)}
.reviews .sec-title{height:75px;padding:16px 12px;border-bottom:1px solid var(--line)}
.reviews .arrows{right:8px;top:34px}
.rv-body{display:flex;padding:28px 0 0 22px}
.badge{width:200px;text-align:center;font-size:13px}
.badge .mark{width:170px;height:70px;margin:0 auto 12px;background:#e9eef5;border-radius:8px}
.badge u{color:#333}
.rv{width:250px;padding-left:38px;font-size:12.5px;line-height:21px;color:#444}
.rv b{font-weight:500;font-size:18px;display:block;color:#222;margin-bottom:6px}
.stars{color:var(--orange);letter-spacing:2px;font-size:17px}
.rv span{color:#888}

/* arrivals */
.arrivals{top:1945px}
.arr-row{display:flex;gap:13px;margin-top:20px;align-items:flex-end;height:368px}
.arr{width:207px;height:300px;background:var(--cream);text-align:center;padding-top:20px;font-size:15px;line-height:23px;color:#222;font-weight:500}
.arr .img{width:130px;height:120px;margin:0 auto 16px;border-radius:50%}
.arr .pr{margin-top:6px;font-weight:400}
.arr u{font-size:13px;font-weight:400}
.arr.hot{width:322px;height:368px;background:var(--orange);color:#fff;font-size:19px;line-height:27px;padding-top:12px}
.arr.hot .img{width:150px;height:170px;margin-bottom:14px}
.arr.hot .btn{display:inline-block;background:#fff;color:#333;font-size:13px;padding:6px 20px;margin-top:10px;font-weight:400}

/* newsletter */
.news{position:absolute;top:2515px;left:0;width:1200px;height:452px;background:linear-gradient(100deg,#6b4a30,#9a6a3c 30%,#3a4f80 50%,#a97a45 75%,#e0a830)}
.news-box{position:absolute;left:211px;top:105px;width:780px;height:300px;background:rgba(255,255,255,.92);text-align:center;padding-top:50px}
.news-box h2{font-family:'Kaushan Script',cursive;font-weight:400;font-size:32px;color:#333}
.news-box p{font-size:17px;margin-top:14px}
.form{display:flex;justify-content:center;gap:16px;margin-top:26px}
.form .in{width:500px;height:52px;border:1px solid #ccc;background:#fff;text-align:left;padding:16px 20px;font-size:13px;color:#999;border-radius:4px}
.form .sub{width:138px;height:52px;background:var(--orange);color:#fff;font-weight:700;font-size:15px;letter-spacing:1px;display:flex;align-items:center;justify-content:center;border-radius:4px}

/* footer */
.footer{position:absolute;top:2967px;left:0;width:1200px;height:425px;background:var(--nav);color:#fff}
.fcol{position:absolute;top:38px;border-left:1px solid #555;padding-left:8px;font-size:12.5px;line-height:31px;height:190px}
.fcol h4{font-weight:400;font-size:17px;margin-bottom:6px}
.contact{left:103px;width:430px}
.contact .row{display:flex;gap:20px;align-items:flex-start;margin-top:6px;font-size:14.5px;line-height:20px}
.contact .row.sm{font-size:12.5px}
.fbottom{position:absolute;top:255px;left:111px;width:977px;border-top:1px solid #555;height:110px}
.copy{position:absolute;left:0;top:58px;font-size:13px;line-height:22px}
.flogo{position:absolute;left:312px;top:40px;font-weight:700;font-size:42px;letter-spacing:6px;color:var(--orange);line-height:1}
.flogo small{display:block;font-size:14px;letter-spacing:10px;color:#fff;text-align:right;margin-top:4px}
.vsep{position:absolute;top:30px;width:1px;height:62px;background:#555}
.social{position:absolute;right:0;top:55px;display:flex;gap:20px}
.social i{display:block;width:26px;height:26px;border-radius:50%;border:2px solid #ddd}
.pay{position:absolute;top:3392px;left:0;width:1200px;height:85px;display:flex;justify-content:center;align-items:center;gap:18px}
.pay i{display:block;width:40px;height:24px;border-radius:4px;background:#d9d9d9}
</style>
</head>
<body>

<header class="header">
  <div class="brand">IRONLINE<small>WORKWEAR</small></div>
  <div class="account">
    <svg width="28" height="28" viewBox="0 0 28 28"><circle cx="14" cy="14" r="14" fill="#222"/><circle cx="14" cy="11" r="5" fill="#fff"/><path d="M5 23c2-5 16-5 18 0" fill="#fff"/></svg>
    <span>Sign In or <a>Register</a></span>
  </div>
  <svg class="cart" width="30" height="26" viewBox="0 0 30 26"><path d="M3 9h18l-2 15H5z" fill="none" stroke="#222" stroke-width="2"/><path d="M8 9V6a4 4 0 0 1 8 0v3" fill="none" stroke="#222" stroke-width="2"/><circle cx="22" cy="7" r="7" fill="#f25c05"/><text x="22" y="10" font-size="9" fill="#fff" text-anchor="middle" font-family="Roboto,sans-serif">0</text></svg>
  <div class="search">Search<i class="dot"></i></div>
</header>

<nav class="nav">
  <span>WORK BOOTS</span><span>WORKWEAR</span><span>CUSTOMIZE IT</span><span>HARD HATS</span><span>GLOVES</span><span>HIGH VIS</span><span>SAFETY GLASSES</span><span>SEE MORE</span>
</nav>

<section class="hero">
  <div class="hero-copy">
    <div class="script">Protection</div>
    <h1>New<br>Workwear<br>Collection.</h1>
    <div class="btn-outline">Shop Now
      <svg width="30" height="12" viewBox="0 0 30 12"><path d="M0 6h27M21 1l6 5-6 5" fill="none" stroke="#333" stroke-width="2"/></svg>
    </div>
  </div>
  <div class="hero-img ph" role="img" aria-label="Safety gear arranged on a dark surface: hard hats, jacket, ear defenders, boots and glasses"></div>
</section>

<section class="promos">
  <div class="promo g">
    <div class="ph" role="img" aria-label="Worker wearing yellow construction gloves using a drill" style="position:absolute;inset:0"></div>
    <div class="s1 script">Construction Safety</div>
    <div class="s2 script">Gloves</div>
    <div class="btn">Shop Now</div>
  </div>
  <div class="promo j">
    <div class="ph" role="img" aria-label="Close-up of an orange hooded duck jacket" style="position:absolute;inset:0"></div>
    <div class="jacket-box"><div class="v">HOODED<br>DUCK<br>JACKET</div><div class="pct">20%</div><div class="off">OFF</div></div>
  </div>
  <div class="promo w">
    <div class="ph" role="img" aria-label="Welder in protective gear with sparks" style="position:absolute;inset:0"></div>
    <div class="w50 script">50%</div>
    <div class="wcon script">Construction</div>
    <div class="wtag script">Workwear</div>
  </div>
</section>

<section class="wrap featured">
  <div class="sec-title"><h2><em>Featured</em> Products</h2><div class="arrows"><i class="a1"></i><i class="a2"></i></div></div>
  <div class="cards">
    <div class="card"><div class="img ph" role="img" aria-label="Orange high-visibility jacket" style="background:linear-gradient(#f8a23a,#e8761a)"></div><div class="n">Vantor EH Soft<br>Toe Boots - VT50260</div><s>$399.00</s><div class="p">$359.00</div><div class="b">Shop Now</div></div>
    <div class="card"><div class="img ph" role="img" aria-label="Yellow hard hat" style="background:linear-gradient(#f7e070,#e9bd10)"></div><div class="n">Vantor EH Soft<br>Toe Boots - VT50260</div><s>$399.00</s><div class="p">$359.00</div><div class="b">Shop Now</div></div>
    <div class="card"><div class="img ph" role="img" aria-label="Clear safety glasses with orange arms" style="background:linear-gradient(#f4f4f4,#f3d9bf)"></div><div class="n">Vantor EH Soft<br>Toe Boots - VT50260</div><s>$399.00</s><div class="p">$359.00</div><div class="b">Shop Now</div></div>
    <div class="card"><div class="img ph" role="img" aria-label="Pair of black and orange work gloves" style="background:linear-gradient(#666,#f0a050)"></div><div class="n">Vantor EH Soft<br>Toe Boots - VT50260</div><s>$399.00</s><div class="p">$359.00</div><div class="b">Shop Now</div></div>
    <div class="card"><div class="img ph" role="img" aria-label="Orange safety vest" style="background:linear-gradient(#ff6a2a,#e14a10)"></div><div class="n">Vantor EH Soft<br>Toe Boots - VT50260</div><s>$399.00</s><div class="p">$359.00</div><div class="b">Shop Now</div></div>
  </div>
</section>

<section class="wrap reviews">
  <div class="sec-title"><h2><em>What Our</em> Customers Are Saying</h2><div class="arrows"><i class="a1"></i><i class="a2"></i></div></div>
  <div class="rv-body">
    <div class="badge"><div class="mark"></div>Based on <u>3,967 reviews</u></div>
    <div class="rv"><b>Dana K. Moss</b><div class="stars">★★★★★</div>Lorem Ipsum is simply dummy text of the printing and typesetting industry. Ever since the 1500s, <span>&nbsp;1 Day ago</span></div>
    <div class="rv"><b>Dana K. Moss</b><div class="stars">★★★★★</div>Lorem Ipsum is simply dummy text of the printing and typesetting industry. Ever since the 1500s, <span>&nbsp;1 Day ago</span></div>
    <div class="rv"><b>Dana K. Moss</b><div class="stars">★★★★★</div>Lorem Ipsum is simply dummy text of the printing and typesetting industry. Ever since the 1500s, <span>&nbsp;1 Day ago</span></div>
  </div>
</section>

<section class="wrap arrivals">
  <div class="sec-title"><h2><em>New</em> Arrivals</h2><div class="arrows"><i class="a1"></i><i class="a2"></i></div></div>
  <div class="arr-row">
    <div class="arr"><div class="img ph" role="img" aria-label="Yellow latex coated gloves" style="background:#e3a62a"></div>Double Dipped Sandy<br>Latex Coated Gloves<br>- Single Pair<div class="pr">$79.00</div><u>Shop Now</u></div>
    <div class="arr"><div class="img ph" role="img" aria-label="Orange hard hat" style="background:#f07a1a"></div>Double Dipped Sandy<br>Latex Coated Gloves<br>- Single Pair<div class="pr">$79.00</div><u>Shop Now</u></div>
    <div class="arr hot"><div class="img ph" role="img" aria-label="Vented cap style hard hat with yellow ear defenders" style="background:linear-gradient(#e8c220,#d9a47a);border-radius:50% 50% 10px 10px"></div>Vented Cap Style<br>Hard Hat 4-Point Ratchet<br>Suspension<div style="margin-top:4px">$99.00</div><div class="btn">Shop Now</div></div>
    <div class="arr"><div class="img ph" role="img" aria-label="Clear safety goggles" style="background:#dcd8e6"></div>Double Dipped Sandy<br>Latex Coated Gloves<br>- Single Pair<div class="pr">$79.00</div><u>Shop Now</u></div>
  </div>
</section>

<section class="news">
  <div class="ph" role="img" aria-label="Flat lay of safety gear on wooden boards: gloves, vest, goggles, hard hats, respirator" style="position:absolute;inset:0"></div>
  <div class="news-box">
    <h2>Join our Newsletter</h2>
    <p>Eque porro quisquam est qui dolorem ipsum quia dolor sit amet</p>
    <div class="form"><div class="in">Your Email Address</div><div class="sub">SUBSCRIBE</div></div>
  </div>
</section>

<footer class="footer">
  <div class="fcol contact">
    <h4>Contact Us</h4>
    <div class="row sm"><svg width="16" height="20" viewBox="0 0 16 20"><path d="M8 0a7 7 0 0 1 7 7c0 5-7 13-7 13S1 12 1 7a7 7 0 0 1 7-7z" fill="#f25c05"/><circle cx="8" cy="7" r="2.5" fill="#262626"/></svg><div>ADDRESS<br>2180 Calder Avenue<br>Millbrook, AL 35400</div></div>
    <div class="row"><svg width="18" height="18" viewBox="0 0 18 18"><path d="M3 1l4 4-2 3c1 2 3 4 5 5l3-2 4 4-3 3C8 17 1 10 0 4z" fill="#f25c05"/></svg><div>Phone: +100 555 0147</div></div>
    <div class="row"><svg width="18" height="14" viewBox="0 0 18 14"><rect width="18" height="14" fill="#f25c05"/><path d="M0 0l9 7 9-7" fill="none" stroke="#262626" stroke-width="1.5"/></svg><div>E-mail: hello@ironlineworkwear.com</div></div>
  </div>
  <div class="fcol" style="left:547px;width:200px"><h4>Quick links</h4>Terms of Use<br>Privacy Policy<br>Payment Methods<br>Refund Policy</div>
  <div class="fcol" style="left:753px;width:180px"><h4>Quick links</h4>Work Boots<br>Workwear<br>Customize It<br>Hard Hats<br>Gloves</div>
  <div class="fcol" style="left:937px;width:160px"><h4>My Account</h4>Shipping<br>Contact Us<br>About us<br>Download our Catalogue</div>
  <div class="fbottom">
    <div class="copy">Ironline Workwear © 2024.<br>All Rights Reserved.</div>
    <div class="vsep" style="left:257px"></div>
    <div class="flogo">IRONLINE<small>WORKWEAR</small></div>
    <div class="vsep" style="left:746px"></div>
    <div class="social"><i></i><i></i><i></i><i></i></div>
  </div>
</footer>

<div class="pay"><i></i><i></i><i></i><i></i><i></i><i></i><i></i></div>

</body>
</html>
```